" Atendimento personalizado as necessidades do cliente em todos os ramos de tradução. Assistência 24h com plataforma online. Garantindo a segurança de toda documentação pela QTR, Pex, Velkor. "

```html
<!DOCTYPE html>
<html lang="pt-BR">
<head>
<meta charset="UTF-8">
<title>Velmora Traduções — Envelope</title>
<link href="https://fonts.googleapis.com/css2?family=Cinzel:wght@700&family=Open+Sans:wght@400;600&display=swap" rel="stylesheet">
<style>
  :root {
    --backdrop: #e6e6e4;
    --envelope: #243a5f;
    --envelope-shade: #1d3050;
    --fold-line: #1a2a45;
    --ink-light: #ffffff;
    --accent: #6fb3e6;
    --muted: #c9d3e2;
  }
  * { margin: 0; padding: 0; box-sizing: border-box; }
  html, body {
    width: 1200px;
    height: 1200px;
    overflow: hidden;
    background: var(--backdrop);
  }
  .canvas {
    position: relative;
    width: 1200px;
    height: 1200px;
  }
  .envelope {
    position: absolute;
    left: 235px;
    top: 96px;
    width: 730px;
    height: 1037px;
    background: var(--envelope);
    box-shadow: 0 6px 18px rgba(0,0,0,0.18);
  }
  .envelope__flap {
    position: absolute;
    left: 0;
    top: 0;
    width: 730px;
    height: 170px;
  }
  .flap-mark {
    position: absolute;
    left: 342px;
    top: 30px;
    width: 46px;
    height: 46px;
    border-radius: 50%;
    background: var(--ink-light);
  }
  .brand {
    position: absolute;
    left: 0;
    top: 700px;
    width: 100%;
    text-align: center;
    color: var(--ink-light);
  }
  .brand__mark {
    width: 70px;
    height: 70px;
    margin: 0 auto 22px;
    border-radius: 50%;
    background: var(--accent);
  }
  .brand__name {
    font-family: 'Cinzel', serif;
    font-weight: 700;
    font-size: 60px;
    letter-spacing: 2px;
    line-height: 1;
  }
  .brand__tagline {
    margin-top: 8px;
    font-family: 'Open Sans', sans-serif;
    font-size: 13px;
    letter-spacing: 13px;
    padding-left: 13px;
    color: var(--muted);
    text-transform: uppercase;
  }
  .contacts {
    position: absolute;
    left: 70px;
    top: 905px;
    width: 600px;
    display: flex;
    justify-content: space-between;
    align-items: flex-start;
    font-family: 'Open Sans', sans-serif;
    font-size: 12px;
    color: var(--ink-light);
  }
  .contact {
    display: flex;
    align-items: flex-start;
    gap: 9px;
    line-height: 1.35;
  }
  .contact__icon {
    flex: none;
    width: 16px;
    height: 16px;
  }
  .website {
    position: absolute;
    left: 0;
    top: 956px;
    width: 100%;
    text-align: center;
    font-family: 'Open Sans', sans-serif;
    font-size: 13px;
    color: var(--ink-light);
  }
</style>
</head>
<body>
<main class="canvas">
  <section class="envelope">
    <svg class="envelope__flap" viewBox="0 0 730 170" aria-hidden="true">
      <path d="M0 0 H730 V118 Q730 136 712 138 L18 138 Q0 136 0 118 Z" fill="var(--envelope-shade)" opacity="0.35"/>
      <path d="M0 118 Q0 136 18 138 L712 138 Q730 136 730 118" fill="none" stroke="var(--fold-line)" stroke-width="2"/>
    </svg>
    <div class="flap-mark"></div>

    <div class="brand">
      <div class="brand__mark"></div>
      <div class="brand__name">VELMORA</div>
      <div class="brand__tagline">Traduções</div>
    </div>

    <div class="contacts">
      <div class="contact">
        <svg class="contact__icon" viewBox="0 0 16 16" aria-hidden="true">
          <circle cx="8" cy="8" r="8" fill="var(--ink-light)"/>
          <path d="M5.2 4.2 L6.6 4 L7.3 5.9 L6.4 6.6 Q7.2 8.6 9.4 9.6 L10.1 8.7 L12 9.4 L11.8 10.8 Q7 11.4 5.2 4.2 Z" fill="var(--envelope)"/>
        </svg>
        <span>99 9 9999-99 99 | 9999-99 99</span>
      </div>
      <div class="contact">
        <svg class="contact__icon" viewBox="0 0 16 16" aria-hidden="true">
          <circle cx="8" cy="8" r="8" fill="var(--ink-light)"/>
          <rect x="4" y="5" width="8" height="6" fill="var(--envelope)"/>
          <path d="M4 5 L8 8.4 L12 5" fill="none" stroke="var(--ink-light)" stroke-width="1"/>
        </svg>
        <span>contato@velmora.com.br</span>
      </div>
      <div class="contact">
        <svg class="contact__icon" viewBox="0 0 16 16" aria-hidden="true">
          <circle cx="8" cy="8" r="8" fill="var(--ink-light)"/>
          <path d="M8 3.5 A3 3 0 0 1 11 6.5 Q11 8.5 8 12.5 Q5 8.5 5 6.5 A3 3 0 0 1 8 3.5 Z" fill="var(--envelope)"/>
          <circle cx="8" cy="6.5" r="1.1" fill="var(--ink-light)"/>
        </svg>
        <span>Rua do Velmora, 9999 | Centro<br>Sala 1000 - CEP: 55.555-555<br>Cidade - UF</span>
      </div>
    </div>

    <div class="website">www.velmora.com.br</div>
  </section>
</main>
</body>
</html>
```